Commerical Office Furniture Company Needs Truck Wrap Design for Box Truck

We need a truck wrap design (and business card) for our company based in Fresno, California. We offer commercial office furnishings such as private office desks, cubicle stations, conference tables, all office seating (task chairs, guest, lobby/lounge, conference) storage systems, ergonomic solutions (monitor arms, keyboard trays, lift desks) and much more. We are a full service office furniture dealer who can fully outfit every space and need for a new or existing office space. We also offer design and space planning services and professional installation.
We would like our trap wrap to be modern using the same color scheme as our logo with a clean but eye catching look. Perhaps using a few nice looking desk/workstations product images as examples to show people what we are capable of. We attached some examples of some themes/layouts we like. feel free to be creative. Our website tembrolight.com has some images and info.
https://imagelibrary.brv-corp.com/detail/client-space-shared-prism-workstation-with-t-line-storage-height-adjustable-tables-and-dorval-seating
Target Market(s)
Private Sector, Education, Healthcare
Industry/Entity Type
Requirements
Must have
- Varto Box Truck - 190 inches x 85 inches

```html
<!DOCTYPE html>
<html lang="en">
<head>
<meta charset="utf-8">
<title>Tembrolight Office Interiors – Box Truck Wrap</title>
<link rel="stylesheet" href="https://fonts.googleapis.com/css2?family=Arimo:wght@400;500&family=Montserrat:wght@500;700&display=swap">
<style>
  :root {
    --page-bg: #3d444c;
    --wrap-white: #f3f5f8;
    --brand-blue: #3b6bbd;
    --stripe-deep: #1f6fc0;
    --stripe-light: #63c5ea;
    --ink-grey: #3f4347;
    --text-white: #ffffff;
  }
  * { margin: 0; padding: 0; box-sizing: border-box; }
  html, body { width: 1200px; height: 772px; overflow: hidden; background: var(--page-bg); }
  .truck-side {
    position: absolute; left: 60px; top: 89px;
    width: 1080px; height: 594px;
    background: var(--wrap-white);
    overflow: hidden;
  }
  .wrap-graphics { position: absolute; inset: 0; width: 100%; height: 100%; }
  .brand-name {
    position: absolute; left: 93px; top: 56px;
    display: flex; align-items: center; gap: 12px;
    font-family: "Arimo", sans-serif; font-weight: 500;
    font-size: 40px; line-height: 1;
    color: var(--brand-blue);
  }
  .brand-name::before {
    content: ""; width: 26px; height: 26px; background: var(--brand-blue);
  }
  .company-title {
    position: absolute; left: 417px; top: 38px; width: 465px;
    font-family: "Arimo", sans-serif; color: var(--brand-blue);
  }
  .company-title .line-main {
    font-size: 40px; font-weight: 500; line-height: 1; white-space: nowrap;
  }
  .company-title .line-sub {
    display: flex; align-items: center; gap: 12px;
    margin-top: 10px; color: var(--ink-grey);
    font-size: 28px; letter-spacing: 14px; line-height: 1;
  }
  .company-title .line-sub::before,
  .company-title .line-sub::after {
    content: ""; flex: 1; height: 3px; background: var(--ink-grey);
  }
  .company-title .line-sub::after { margin-left: -14px; }
  .services {
    margin-top: 10px; color: var(--ink-grey);
    font-size: 20px; display: flex; justify-content: space-between;
  }
  .contact-phone {
    position: absolute; left: 118px; top: 532px;
    display: flex; align-items: center; gap: 14px;
    font-family: "Montserrat", sans-serif; font-weight: 700;
    font-size: 36px; color: var(--text-white);
  }
  .contact-phone svg { width: 42px; height: 42px; }
  .contact-web {
    position: absolute; right: 28px; top: 543px;
    font-family: "Montserrat", sans-serif; font-weight: 500;
    font-size: 24px; color: var(--text-white);
  }
</style>
</head>
<body>
  <main class="truck-side">
    <svg class="wrap-graphics" viewBox="0 0 1010 555" preserveAspectRatio="none">
      <polygon class="band-deep" points="0,232 535,475 1010,250 1010,555 0,555" fill="var(--stripe-deep)"/>
      <polygon class="band-light" points="0,250 535,490 1010,268 1010,555 0,555" fill="var(--stripe-light)"/>
      <polygon class="band-main" points="0,300 535,510 1010,325 1010,555 0,555" fill="var(--brand-blue)"/>

      <defs>
        <linearGradient id="office-grey" x1="0" y1="0" x2="0" y2="1">
          <stop offset="0" stop-color="#c9cbcd"/><stop offset="1" stop-color="#5b5657"/>
        </linearGradient>
        <linearGradient id="workstation-tone" x1="0" y1="0" x2="0" y2="1">
          <stop offset="0" stop-color="#d6d8da"/><stop offset="0.55" stop-color="#5a4a48"/><stop offset="1" stop-color="#9a9c9e"/>
        </linearGradient>
        <linearGradient id="wood-tone" x1="0" y1="0" x2="0" y2="1">
          <stop offset="0" stop-color="#a9b2b8"/><stop offset="0.35" stop-color="#7a3f28"/><stop offset="1" stop-color="#8e4b2c"/>
        </linearGradient>
      </defs>

      <g class="product-photos" stroke="#ffffff" stroke-width="12" stroke-linejoin="miter">
        <polygon role="img" aria-label="Photo of a glass-walled private office with dark laminate desks"
          points="180,230 290,188 400,230 400,375 290,445 180,375" fill="url(#office-grey)"/>
        <polygon role="img" aria-label="Photo of a U-shaped executive workstation with overhead storage and frosted glass doors"
          points="400,235 535,162 665,235 665,410 535,480 400,410" fill="url(#workstation-tone)"/>
        <polygon role="img" aria-label="Photo of a cherry wood executive desk with a leather office chair"
          points="665,255 765,202 865,255 865,400 765,445 665,400" fill="url(#wood-tone)"/>
      </g>
    </svg>

    <div class="brand-name">Tembrolight</div>

    <div class="company-title">
      <div class="line-main">TEMBROLIGHT OFFICE</div>
      <div class="line-sub">INTERIORS</div>
      <div class="services"><span>Office Furniture</span><span>•</span><span>Design</span><span>•</span><span>Installation</span></div>
    </div>

    <div class="contact-phone">
      <svg viewBox="0 0 44 44" aria-hidden="true">
        <circle cx="22" cy="22" r="21" fill="#ffffff"/>
        <path d="M15 11c1-1 2.5-1 3.3.2l2.3 3.4c.7 1 .5 2.3-.4 3.1l-1.6 1.4c1 2.6 3 4.8 5.6 6l1.5-1.6c.8-.9 2.2-1 3.1-.3l3.4 2.4c1.1.8 1.2 2.3.2 3.3l-1.8 1.9c-1.4 1.4-3.5 1.8-5.3 1-6.4-2.8-11-7.6-13.5-14-.7-1.8-.2-3.9 1.2-5.2z" fill="var(--brand-blue)"/>
      </svg>
      <span>555-201-4780</span>
    </div>

    <div class="contact-web">tembrolight.com</div>
  </main>
</body>
</html>
```